Car rental website design for a UAE car rental company

This project is about creating a new website design for a car rental company located in Dubai (United Arab Emirates), I opened the same project a few months ago but I didn't receive a lot of appealing entries so I closed it but this time I am marking the project as guaranteed to avoid such situation again, if you have already provided a design before then please re-submit again on this project so that it is considered while reviewing all the designs

A few important things:

1- We need a simple non-complex design
2- The final deliverable would be 2 screens (PSD, JPEG ... etc), the first screen is for the home page and the second screen is for an internal page
3- The home page must have a section that end users can use to rent a car online directly from the home page instead of going into some inner pages
4- The current website is very old and not very appealing so avoid creating a similar design (www.runo-vexa.example)
5- The name is Runovexa but the company rents normal cars (no Limousin cars will be rented) so avoid adding any fancy cars in the images/graphics used in the design, just normal end users cars
6- The expected pages would be: home, About us, Our team, Strategy, Contact us and links to social media pages
7- The attachments include the company's logo and some screens from other car rental companies that provide online rentals/payments

If you have any questions please feel free to ask and please note that we will need the designs urgently

Thanks

Target Market(s)

Dubai - United Arab Emirates

Industry/Entity Type

It Company

Number of Pages Required

2 page

Font styles to use
Sans Serif

Requirements
Must have
• Check the project details
Nice to have
Should not have

```html
<!DOCTYPE html>
<html lang="en">
<head>
<meta charset="utf-8">
<title>Runovexa – Rent A Car</title>
<link rel="stylesheet" href="https://fonts.googleapis.com/css2?family=Open+Sans:wght@400;600;700;800&display=swap">
<style>
:root{
  --crimson:#a3093a;
  --black:#050505;
  --ink:#0d0d0d;
  --footer:#111111;
  --white:#ffffff;
  --text-grey:#7a7a7a;
  --title-grey:#6f6f6f;
  --rule:#e2e2e2;
  --sand:#ebe9e3;
  --label:#c9c9c9;
  --field:#ffffff;
}
*{margin:0;padding:0;box-sizing:border-box}
html,body{width:1200px;height:2365px;overflow:hidden}
body{font-family:"Open Sans",Arial,sans-serif;background:var(--white);color:var(--text-grey);position:relative}

/* Header */
.site-header{position:absolute;top:0;left:0;width:1200px;height:135px;background:var(--black)}
.brand{position:absolute;left:62px;top:58px;display:flex;align-items:center;gap:12px}
.brand-mark{width:26px;height:26px;background:var(--crimson)}
.brand-name{font-weight:700;font-size:28px;color:var(--white);letter-spacing:.5px}
.main-nav{position:absolute;top:112px;left:436px;display:flex;font-weight:800;font-size:12.5px;color:var(--white);letter-spacing:.3px}
.main-nav a{color:inherit;text-decoration:none;margin-right:0}
.nav-home{position:absolute;left:0}
.nav-about{position:absolute;left:94px;white-space:nowrap}
.nav-team{position:absolute;left:216px;white-space:nowrap}
.nav-strategy{position:absolute;left:340px;white-space:nowrap}
.nav-contact{position:absolute;left:462px;white-space:nowrap}
.social{position:absolute;top:112px;left:1027px;display:flex;gap:26px}
.social span{display:block;width:15px;height:15px;border-radius:50%;background:var(--white)}

/* Hero */
.hero{position:absolute;top:135px;left:0;width:1200px;height:605px;
  background:radial-gradient(ellipse at 30% 40%,#5a5a5a 0%,#2c2c2c 35%,#141414 70%,#0a0a0a 100%)}
.hero-title{position:absolute;top:100px;left:0;width:1200px;text-align:center;color:var(--white);
  font-weight:800;font-size:38px;letter-spacing:9px;line-height:50px}
.hero-sub{position:absolute;top:222px;left:0;width:1200px;text-align:center;color:var(--white);
  font-weight:600;font-size:17px;letter-spacing:3px;line-height:22px}
.btn{display:inline-block;background:var(--crimson);color:var(--white);font-weight:800;font-size:13px;
  letter-spacing:1.5px;text-align:center;text-decoration:none}
.hero .btn{position:absolute;left:508px;top:363px;width:184px;height:44px;line-height:44px}

/* Welcome */
.welcome{position:absolute;top:740px;left:0;width:1200px;height:690px}
.section-title{font-weight:800;color:var(--crimson);font-size:44px;letter-spacing:.5px;text-align:center}
.welcome .section-title{position:absolute;top:78px;width:1200px}
.intro{position:absolute;top:190px;left:320px;width:560px;text-align:center;font-size:14px;line-height:20px}
.intro p+p{margin-top:20px}
.features{position:absolute;top:365px;left:60px;display:flex}
.feature{width:270px;height:236px;text-align:center;border-left:1px solid var(--rule)}
.feature:first-child{border-left:none}
.feature svg{margin-top:40px}
.feature h3{margin-top:14px;font-weight:700;font-size:14px;color:var(--title-grey)}
.feature p{margin-top:22px;font-size:10.5px;line-height:19px;color:#555}

/* Mission */
.mission{position:absolute;top:1430px;left:0;width:1200px;height:355px;display:flex}
.mission-copy{width:600px;height:355px;background:var(--sand);position:relative}
.mission-copy .section-title{position:absolute;top:58px;left:84px;text-align:left}
.mission-copy .body{position:absolute;top:166px;left:86px;width:470px;font-size:14px;line-height:20px}
.mission-copy .body p+p{margin-top:20px}
.mission-photo{width:600px;height:355px;background:linear-gradient(120deg,#3a3a3a 0%,#8c8c8c 40%,#d9d9d9 60%,#6a6a6a 100%)}

/* Booking */
.book-heading{position:absolute;top:1785px;left:0;width:1200px;height:130px}
.book-heading .section-title{line-height:130px}
.booking{position:absolute;top:1915px;left:0;width:1200px;height:380px;background:var(--ink)}
.booking-form{position:absolute;left:74px;top:28px}
.field-label{display:block;font-weight:700;font-size:14px;color:var(--label);line-height:18px}
.field-label small{font-weight:400;font-size:14px}
.field{background:var(--field);height:26px;border:1px solid #999;font-size:13px;color:#333;padding:0 6px;line-height:24px;position:relative}
.row{display:flex;gap:10px;margin-top:2px}
.group{margin-bottom:12px}
.field.wide{width:286px}
.field.date{width:182px}
.field.time{width:182px}
.field svg{position:absolute;top:3px;right:4px}
.booking .btn{width:184px;height:44px;line-height:44px;margin-top:10px}
.car-photo{position:absolute;left:642px;top:35px;width:508px;height:315px;
  background:linear-gradient(180deg,#ffffff 0%,#f4f4f4 60%,#dedede 100%)}

/* Footer */
.site-footer{position:absolute;top:2295px;left:0;width:1200px;height:70px;background:var(--footer);
  text-align:center;line-height:70px;font-size:11px;color:#bdbdbd}
</style>
</head>
<body>

<header class="site-header">
  <div class="brand"><span class="brand-mark"></span><span class="brand-name">Runovexa</span></div>
  <nav class="main-nav">
    <a class="nav-home" href="#">HOME</a>
    <a class="nav-about" href="#">ABOUT US</a>
    <a class="nav-team" href="#">OUR TEAM</a>
    <a class="nav-strategy" href="#">STRATEGY</a>
    <a class="nav-contact" href="#">CONTACT US</a>
  </nav>
  <div class="social" aria-label="Social media links"><span></span><span></span><span></span></div>
</header>

<section class="hero" role="img" aria-label="Dark monochrome photo of a car interior with gear stick and seats">
  <h1 class="hero-title">WE WON OUR CLIENTS' RESPECT<br>AND RECOGNITION</h1>
  <p class="hero-sub">because of our dedication and professionalism<br>in the business.</p>
  <a class="btn" href="#">BOOK A CAR</a>
</section>

<section class="welcome">
  <h2 class="section-title">WELCOME TO RUNOVEXA</h2>
  <div class="intro">
    <p>To be one of the leading auto leasing company in the fast growing economy and tourism industry of the emirate of Dubai and play alongside with the major car rental companies in the globe.</p>
    <p>Runovexa vows to deliver comfort, luxury and satisfaction to all our clients by providing them professional, hassle-free and first-class service.</p>
  </div>
  <div class="features">
    <div class="feature">
      <svg width="24" height="26" viewBox="0 0 24 26" fill="none" stroke="#a3093a" stroke-width="1.5"><circle cx="12" cy="12" r="5.5"/><path d="M10 17.5v3h4v-3M12 1v3M3 4l2 2M21 4l-2 2M0.5 12h3M20.5 12h3"/></svg>
      <h3>Title goes here</h3>
      <p>consectetur adipisicing elit, sedo<br>eiusmod tempor incidi<br>et dolorsersrs eerhfre mag.</p>
    </div>
    <div class="feature">
      <svg width="24" height="26" viewBox="0 0 24 26" fill="none" stroke="#a3093a" stroke-width="1.5"><path d="M4 20l2-6L17 3l4 4L10 18z M4 20l6-2M15 5l4 4"/></svg>
      <h3>Title goes here</h3>
      <p>consectetur adipisicing elit, sedo<br>eiusmod tempor incidi<br>et dolorsersrs eerhfre mag.</p>
    </div>
    <div class="feature">
      <svg width="24" height="26" viewBox="0 0 24 26" fill="none" stroke="#a3093a" stroke-width="1.5"><circle cx="12" cy="13" r="4"/><circle cx="12" cy="13" r="9" stroke-dasharray="4 2.6"/></svg>
      <h3>Title goes here</h3>
      <p>consectetur adipisicing elit, sedo<br>eiusmod tempor incidi<br>et dolorsersrs eerhfre mag.</p>
    </div>
    <div class="feature">
      <svg width="24" height="26" viewBox="0 0 24 26" fill="none" stroke="#a3093a" stroke-width="1.5"><rect x="4" y="6" width="16" height="11"/><path d="M1 20h22"/></svg>
      <h3>Title goes here</h3>
      <p>consectetur adipisicing elit, sedo<br>eiusmod tempor incidi<br>et dolorsersrs eerhfre mag.</p>
    </div>
  </div>
</section>

<section class="mission">
  <div class="mission-copy">
    <h2 class="section-title">MISSION &amp; VISION</h2>
    <div class="body">
      <p>To be one of the leading auto leasing company in the fast growing economy and tourism industry of the emirate of Dubai and play alongside with the major car rental companies in the globe.</p>
      <p>Runovexa vows to deliver comfort, luxury and satisfaction to all our clients by providing them professional, hassle-free and first-class service.</p>
    </div>
  </div>
  <div class="mission-photo" role="img" aria-label="Black and white photo of a car side mirror reflecting the road"></div>
</section>

<div class="book-heading"><h2 class="section-title">BOOK A CAR</h2></div>

<section class="booking">
  <form class="booking-form">
    <div class="group">
      <label class="field-label">Pick-up Location <small>(City, State or Airport Code)</small></label>
      <div class="row"><div class="field wide">Dubai Airport - Terminal 3</div></div>
    </div>
    <div class="group">
      <label class="field-label">Pick-up Date and Time:</label>
      <div class="row">
        <div class="field date">30/03/2015<svg width="18" height="18" viewBox="0 0 18 18"><rect x="1" y="3" width="16" height="14" fill="#ddd" stroke="#555"/><rect x="1" y="3" width="16" height="4" fill="#555"/><path d="M4 10h2M8 10h2M12 10h2M4 13h2M8 13h2M12 13h2" stroke="#555"/></svg></div>
        <div class="field time">16:00<svg width="12" height="18" viewBox="0 0 12 18"><path d="M2 7l4-5 4 5zM2 11l4 5 4-5z" fill="#222"/></svg></div>
      </div>
    </div>
    <div class="group">
      <label class="field-label">Return Date and Time:</label>
      <div class="row">
        <div class="field date">31/03/2015<svg width="18" height="18" viewBox="0 0 18 18"><rect x="1" y="3" width="16" height="14" fill="#ddd" stroke="#555"/><rect x="1" y="3" width="16" height="4" fill="#555"/><path d="M4 10h2M8 10h2M12 10h2M4 13h2M8 13h2M12 13h2" stroke="#555"/></svg></div>
        <div class="field time">16:00<svg width="12" height="18" viewBox="0 0 12 18"><path d="M2 7l4-5 4 5zM2 11l4 5 4-5z" fill="#222"/></svg></div>
      </div>
    </div>
    <div class="group">
      <label class="field-label">Hire Car Type:</label>
      <div class="row"><div class="field wide">Automatic<svg width="16" height="18" viewBox="0 0 16 18"><path d="M2 6l6 6 6-6" fill="none" stroke="#222" stroke-width="2.5"/></svg></div></div>
    </div>
    <a class="btn" href="#">BOOK A CAR</a>
  </form>
  <div class="car-photo" role="img" aria-label="Photo of a white compact hatchback on a white background"></div>
</section>

<footer class="site-footer">©Copyright 2011, Runovexa. All rights reserved.</footer>

</body>
</html>
```